Australian Trucking Company Requires Professional Looking Stationary

We require a professional looking stationary design that incorporates our newly designed logo.

Our business, called "Marlow Haul Contracting", provides contracting work, transport and logistics to business in Western Australia particularly with links to the mining sector.

We are a small business looking to expand and our new logo and our new stationary will help develop our brand image in our market place.

Target Market(s)

Businesses and Corporation with links to the Mining Sector

Industry/Entity Type

Small Business

Requirements
Must have
• The letterhead must have the following details:
The new logo

Text saying: "Marlow Holdings Pty Ltd (ACN 352 018 927) ATF The Marlow Discretionary Trust T/AS"
"ABN 72 483 910 615"
Address "P.O Box 817 Wexbridge WA, 6999"
Phone: 08 9555 0182
Email: marlowhaul@inboxmail.example

The text on the letterhead should be editable as the details are likely to change in the near future. Provision should be made for a website address all though one isn't available at the moment.

The styling, layout and font text is entirely up to the designer.

```html
<!DOCTYPE html>
<html lang="en">
<head>
<meta charset="utf-8">
<title>Marlow Haul Contracting – Envelopes</title>
<link href="https://fonts.googleapis.com/css2?family=Exo+2:wght@800&family=Roboto:wght@400&display=swap" rel="stylesheet">
<style>
  :root {
    --backdrop: #5b5b5b;
    --paper: #ffffff;
    --brand-red: #e01f27;
    --brand-red-dark: #8d1a1e;
    --ink: #3a3a3a;
    --window-edge: #b9b9b9;
    --window-light: #ffffff;
    --window-shade: #d6d6d7;
    --mark-grey: #9a9a9a;
  }
  html, body {
    margin: 0;
    width: 1200px;
    height: 872px;
    overflow: hidden;
    background: var(--backdrop);
  }
  .canvas {
    position: relative;
    width: 1200px;
    height: 872px;
  }
  .envelope {
    position: absolute;
    background: var(--paper);
    box-shadow: 0 4px 14px rgba(0,0,0,.35);
  }
  .envelope--front {
    left: 157px; top: 148px; width: 635px; height: 277px;
  }
  .brand-band {
    position: absolute;
    left: 86px; top: 26px; width: 549px; height: 48px;
    background: linear-gradient(90deg, var(--brand-red) 0%, var(--brand-red) 45%, var(--brand-red-dark) 100%);
  }
  .brand-mark {
    position: absolute;
    left: 32px; top: 33px; width: 34px; height: 34px;
    background: var(--mark-grey);
  }
  .brand-name {
    font-family: "Exo 2", sans-serif;
    font-weight: 800;
    text-transform: uppercase;
    color: var(--paper);
    margin: 0;
    white-space: nowrap;
  }
  .brand-band .brand-name {
    position: absolute;
    left: 6px; top: 13px;
    font-size: 17px;
    line-height: 22px;
  }
  .address-window {
    position: absolute;
    left: 31px; top: 117px; width: 251px; height: 90px;
    border: 1.5px solid var(--window-edge);
    border-radius: 12px;
    background: linear-gradient(90deg, var(--window-light) 0%, var(--window-shade) 100%);
  }
  .sender-details {
    position: absolute;
    left: 21px; top: 240px;
    font-family: "Roboto", sans-serif;
    font-size: 8.4px;
    line-height: 12px;
    color: var(--ink);
    margin: 0;
  }
  .sender-details p { margin: 0; white-space: nowrap; }
  .sender-details .label { color: var(--brand-red); }
  .sender-details .icon {
    display: inline-block;
    vertical-align: -1px;
    margin: 0 2px 0 6px;
  }
  .envelope--back {
    left: 427px; top: 467px; width: 631px; height: 275px;
    overflow: hidden;
  }
  .flap {
    position: absolute;
    left: 0; top: 0;
  }
  .flap .brand-name {
    position: absolute;
    left: 296px; top: 28px;
    font-size: 13.5px;
    line-height: 15px;
  }
  .flap-mark {
    position: absolute;
    left: 236px; top: 32px; width: 46px; height: 34px;
  }
  .flap-mark span {
    display: block;
    width: 30px; height: 30px;
    margin: 2px 0 0 14px;
    background: rgba(255,255,255,.85);
  }
</style>
</head>
<body>
<main class="canvas">

  <section class="envelope envelope--front" aria-label="Envelope front">
    <div class="brand-mark" aria-hidden="true"></div>
    <div class="brand-band">
      <h1 class="brand-name">Marlow Haul Contracting</h1>
    </div>
    <div class="address-window" aria-label="Address window"></div>
    <div class="sender-details">
      <p>Marlow Holdings Pty Ltd (ACN 352 018 927) ATF The Marlow Discretionary Trust T/AS</p>
      <p><span class="label">ABN</span> 72 483 910 615
        <svg class="icon" width="9" height="8" viewBox="0 0 9 8" aria-hidden="true"><path d="M4.5 0 L9 4 H7.6 V8 H5.4 V5.5 H3.6 V8 H1.4 V4 H0 Z" fill="var(--brand-red)"/></svg>P.O Box 817 Wexbridge WA, 6999
        <svg class="icon" width="11" height="7" viewBox="0 0 11 7" aria-hidden="true"><rect width="11" height="7" rx="1" fill="var(--brand-red)"/><path d="M0.5 0.8 L5.5 4 L10.5 0.8" stroke="#fff" stroke-width=".8" fill="none"/></svg>marlowhaul@inboxmail.example</p>
    </div>
  </section>

  <section class="envelope envelope--back" aria-label="Envelope back">
    <div class="flap">
      <svg width="631" height="92" viewBox="0 0 631 92" aria-hidden="true">
        <defs>
          <linearGradient id="flapRed" x1="0" x2="1" y1="0" y2="0">
            <stop offset="0" stop-color="var(--brand-red)"/>
            <stop offset=".45" stop-color="var(--brand-red)"/>
            <stop offset="1" stop-color="var(--brand-red-dark)"/>
          </linearGradient>
        </defs>
        <path d="M0 0 H631 L604 76 Q598 91 580 91 H51 Q33 91 27 76 Z" fill="url(#flapRed)"/>
      </svg>
      <div class="flap-mark" aria-hidden="true"><span></span></div>
      <p class="brand-name">Marlow Haul<br>Contracting</p>
    </div>
  </section>

</main>
</body>
</html>
```